Kavo Modellwerk.Brenn GmbH needed a letterhead template

For English scroll down. We need a letterhead template and since we already have our logo design successfully with you, we now want to also design the letterhead with you. Down in the uploaded file you see what is important and what should definitely be seen on our template. The template should be like the homepage (www.modellwerk.brenn) held in red, blue and white. We need a letter-head submission. In the bottom in the chapter "databases uploading" you can find the most important things, did must be on the submission. The submission shoulderstand be in the colors blue, red and white like our homepage (www.modellwerk.brenn).

```html
<!DOCTYPE html>
<html lang="en">
<head>
<meta charset="utf-8">
<title>Modellwerk.Brenn GmbH – Letterhead</title>
<link href="https://fonts.googleapis.com/css2?family=Metrophobic&display=swap" rel="stylesheet">
<style>
  :root {
    --brand-blue: #4a8fcf;
    --brand-red: #c8202e;
    --charcoal: #363636;
    --paper: #f3f3f3;
    --ink: #2b2b2b;
    --white: #ffffff;
  }
  * { box-sizing: border-box; margin: 0; padding: 0; }
  html, body { width: 933px; height: 1200px; overflow: hidden; }
  body {
    position: relative;
    background: var(--paper);
    font-family: "Metrophobic", "Segoe UI", sans-serif;
    color: var(--ink);
  }
  .top-band { position: absolute; left: 0; top: 0; width: 933px; height: 47px; background: var(--brand-blue); }
  .top-rule { position: absolute; left: 0; top: 47px; width: 933px; height: 7px; background: var(--charcoal); }
  .bottom-rule { position: absolute; left: 0; top: 1152px; width: 933px; height: 7px; background: var(--charcoal); }
  .bottom-band { position: absolute; left: 0; top: 1159px; width: 933px; height: 41px; background: var(--brand-blue); }

  .brand {
    position: absolute; left: 0; top: 112px; width: 933px;
    display: flex; justify-content: center; align-items: center; gap: 14px;
  }
  .brand-mark { width: 40px; height: 40px; border-radius: 50%; background: var(--brand-blue); }
  .brand-name { font-size: 34px; color: var(--brand-red); letter-spacing: 0.2px; }

  .recipient { position: absolute; left: 118px; top: 242px; font-size: 20px; line-height: 27px; }
  .date { position: absolute; right: 119px; top: 285px; font-size: 15px; letter-spacing: 0.3px; }

  .letter-body {
    position: absolute; left: 118px; top: 343px; width: 696px;
    font-size: 15.4px; line-height: 21.5px;
  }
  .letter-body p + p { margin-top: 21.5px; }
  .letter-body .line { display: block; text-align: justify; text-align-last: justify; }
  .letter-body .line.end { text-align: left; text-align-last: left; }

  .closing { position: absolute; left: 117px; top: 762px; font-size: 20px; }
  .signature { position: absolute; left: 154px; top: 799px; width: 76px; height: 44px;
    background: linear-gradient(90deg, rgba(60,60,60,0.15), rgba(60,60,60,0.05)); border-radius: 4px; }
  .signatory { position: absolute; left: 117px; top: 850px; font-size: 18px; letter-spacing: 0.5px; }

  .contact-bar { position: absolute; left: 13px; top: 1023px; width: 907px; height: 79px; display: flex; }
  .contact-item { flex: 1; display: flex; align-items: center; color: var(--white); font-size: 13.5px; line-height: 17px; }
  .contact-item span { white-space: nowrap; }
  .contact-item.phone { background: var(--brand-blue); padding-left: 59px; }
  .contact-item.web { background: var(--charcoal); padding-left: 59px; font-size: 13px; }
  .contact-item.address { background: var(--brand-blue); padding-left: 63px; }
  .contact-icon { width: 34px; height: 34px; background: var(--white); border-radius: 5px;
    display: flex; align-items: center; justify-content: center; margin-right: 12px; flex: none; }
  .contact-item.phone .contact-icon { margin-right: 20px; }
  .contact-item.web .contact-icon { margin-right: 10px; background: var(--paper); }
</style>
</head>
<body>
  <div class="top-band"></div>
  <div class="top-rule"></div>

  <header class="brand">
    <span class="brand-mark"></span>
    <span class="brand-name">Modellwerk.Brenn</span>
  </header>

  <div class="recipient">Geschäftsführer<br>Dr.&nbsp; Varnholt Emil</div>
  <div class="date">DATE : 20 MAY 2020</div>

  <main class="letter-body">
    <p>
      <span class="line">There are many variations of passages of Lorem Ipsum available, but the majority have suf-</span>
      <span class="line">fered alteration in some form, by injected humour, or randomised words which don't look</span>
      <span class="line">even slightly believable. If you are going to use a passage of Lorem Ipsum, you need to be</span>
      <span class="line end">sure there isn't anything embarrassing hidden in the middle of text. All the Lorem Ipsum...</span>
    </p>
    <p>
      <span class="line">All the Lorem Ipsum generators on the Internet tend to repeat predefined chunks as neces-</span>
      <span class="line">sary, making this the first true generator on the Internet. It uses a dictionary of over 200</span>
      <span class="line end">Latin words,</span>
    </p>
    <p>
      <span class="line">&nbsp;Combined with a handful of model sentence structures, to generate Lorem Ipsum which</span>
      <span class="line">looks reasonable. The generated Lorem Ipsum is therefore always free from repetition, in-</span>
      <span class="line">jected humour, or non-characteristic words etc.All the Lorem Ipsum generators on the Inter-</span>
      <span class="line end">net tend to repeat predefined chunks as necessary, making......</span>
    </p>
    <p>
      <span class="line">There are many variations of passages of Lorem Ipsum available, but the majority have suf-</span>
      <span class="line">fered alteration in some form, by injected humour, or randomised words which don't look</span>
      <span class="line end">even slightly believable. If you are going to use a passage</span>
    </p>
  </main>

  <div class="closing">Sincerely yours:</div>
  <div class="signature" role="img" aria-label="Handwritten signature"></div>
  <div class="signatory">LORENZ AICHER</div>

  <footer class="contact-bar">
    <div class="contact-item phone">
      <span class="contact-icon">
        <svg width="22" height="22" viewBox="0 0 24 24"><path fill="#4a8fcf" d="M6.6 10.8a15.1 15.1 0 0 0 6.6 6.6l2.2-2.2a1 1 0 0 1 1-.25 11.4 11.4 0 0 0 3.6.57 1 1 0 0 1 1 1V20a1 1 0 0 1-1 1A17 17 0 0 1 3 4a1 1 0 0 1 1-1h3.5a1 1 0 0 1 1 1c0 1.25.2 2.45.57 3.57a1 1 0 0 1-.25 1z"/></svg>
      </span>
      <span>:&nbsp; 0800&nbsp; XX&nbsp; XX&nbsp; XX</span>
    </div>
    <div class="contact-item web">
      <span class="contact-icon">
        <svg width="22" height="22" viewBox="0 0 24 24" fill="none" stroke="#363636" stroke-width="2"><circle cx="12" cy="12" r="9"/><ellipse cx="12" cy="12" rx="4" ry="9"/><path d="M3 12h18"/></svg>
      </span>
      <span>Mail:&nbsp; contact@modellwerk.brenn<br>Web:&nbsp; www.modellwerk.brenn</span>
    </div>
    <div class="contact-item address">
      <span class="contact-icon">
        <svg width="22" height="22" viewBox="0 0 24 24"><path fill="#4a8fcf" d="M12 2a7 7 0 0 0-7 7c0 5 7 13 7 13s7-8 7-13a7 7 0 0 0-7-7zm0 9.5A2.5 2.5 0 1 1 12 6.5a2.5 2.5 0 0 1 0 5z"/></svg>
      </span>
      <span>Lindenweg&nbsp; 12<br>6094&nbsp; Brennstal,Tirol<br>Österreich</span>
    </div>
  </footer>

  <div class="bottom-rule"></div>
  <div class="bottom-band"></div>
</body>
</html>
```